Mardolin construction chemical business need advertisement

We need an advertisement as building signboard for a new company called "Mardolin"-meaning truly effective, value added building solution.
-we source the best and effective products around the world that suit the local climate conditions
- we carry varieties of quality construction chemicals products that are cost effective and suitable for any size of budget and project and even for home user DIY .
- we provide consultation and system to solve any building problems. e.g. tiling system, waterproofing system, concrete repair system, green roof system
- We provide products training and waterproofing solutions to our clients and applicators that use our products
-By utilising our products and services, will leverage the value of the properties and protect your investment.
-our mission- to provide consultancy, services to repair, to restpre and to add avlue to properties throughout the lifecycle of the building resulting in greater whole value hence not limited to develiper but to end user protecting their investment with the quality products and services we provide.
- our philosophy-"Passion towards commitment, quality, knowledge, good practice and result.
- we need the advertisement to be easily understand by End user and contractor of the service and product we provide to solve their problem
- yet also look professional to designer and architect
end user, contractor, builder, designer, achitect
Business
- -Please create a slogan, easily to understand at one glance of what type of service and products we provide.
- -less wording, the advertisement will be put at the building
- -Strong message to explain our business

```html
<!DOCTYPE html>
<html lang="en">
<head>
<meta charset="utf-8">
<title>Mardolin – Effective System</title>
<link href="https://fonts.googleapis.com/css2?family=Lato:wght@300;400;700&display=swap" rel="stylesheet">
<style>
  :root {
    --cyan: #14b8dc;
    --cyan-light: #00c3e6;
    --teal: #1a9fc0;
    --charcoal: #2b2b2d;
    --charcoal-soft: #3b3b3e;
    --ink: #1c1c1c;
    --paper: #ffffff;
    --stage: #f1f1f1;
  }
  * { margin: 0; padding: 0; box-sizing: border-box; }
  html, body { width: 1200px; height: 1200px; overflow: hidden; }
  body { background: var(--stage); font-family: "Lato", sans-serif; color: var(--ink); position: relative; }

  .flyer {
    position: absolute; left: 185px; top: 18px;
    width: 938px; height: 1316px;
    background: var(--paper);
    transform: scale(0.885); transform-origin: top left;
    overflow: hidden;
  }
  .hero-photo {
    position: absolute; left: 0; top: 0; width: 938px; height: 600px;
    background: linear-gradient(155deg, #5e9fe0 0%, #8cc0ea 22%, #3b62a8 45%, #243f86 62%, #b8603c 82%, #c9714a 100%);
  }
  .hero-bands { position: absolute; left: 0; top: 0; width: 938px; height: 900px; }

  .headline { position: absolute; left: 42px; top: 608px; }
  .headline-kicker { font-weight: 700; font-size: 62px; color: var(--cyan); letter-spacing: 1px; line-height: 1; }
  .headline-main { font-weight: 300; font-size: 112px; color: var(--paper); line-height: 1; margin-top: 4px; letter-spacing: -1px; }

  .inset-photo {
    position: absolute; left: 588px; top: 617px; width: 286px; height: 166px;
    border: 2px solid var(--paper);
    background: linear-gradient(180deg, #dfe9f2 0%, #aebfcf 45%, #6f8aa0 75%, #3f7a86 100%);
  }

  .section-title { font-weight: 700; font-size: 21px; color: var(--ink); }
  .body-text { font-size: 15px; line-height: 18.5px; }
  .bullet-list { list-style: none; display: grid; grid-template-columns: 226px 1fr; row-gap: 5px; font-size: 15px; }
  .bullet-list li::before { content: "•"; color: var(--teal); margin-right: 5px; }

  .provide { position: absolute; left: 44px; top: 910px; width: 400px; }
  .provide .body-text { margin-top: 16px; }
  .provide .bullet-list { margin-top: 8px; }

  .mission { position: absolute; left: 44px; top: 1046px; width: 394px; }
  .mission .bullet-list { margin-top: 14px; grid-template-columns: 268px 1fr; }
  .mission .body-text { margin-top: 14px; text-align: justify; }

  .promise { position: absolute; left: 508px; top: 870px; font-size: 23.5px; line-height: 28px; }
  .promise-accent { color: var(--cyan); font-size: 29.5px; line-height: 34px; }

  .philosophy { position: absolute; left: 492px; top: 988px; width: 420px; }
  .tick-list { list-style: none; display: grid; grid-template-columns: 224px 1fr; row-gap: 6px; margin-top: 20px; font-size: 15px; line-height: 18px; }
  .tick-list li { display: flex; gap: 5px; }
  .tick-list svg { flex: none; margin-top: 3px; }
  .tick-col { display: flex; flex-direction: column; gap: 6px; }

  .brand-backdrop {
    position: absolute; left: 740px; top: 1090px; width: 198px; height: 168px;
    background: radial-gradient(ellipse at 70% 60%, #e4e6e8 0%, #f2f3f4 50%, rgba(255,255,255,0) 80%);
  }
  .brand-name {
    position: absolute; left: 600px; top: 1138px; width: 200px; text-align: center;
    font-weight: 400; font-size: 42px; color: var(--cyan);
  }

  .footer {
    position: absolute; left: 0; top: 1258px; width: 938px; height: 58px;
    background: var(--charcoal);
    display: flex; align-items: center; justify-content: center;
    color: var(--paper); font-size: 18px; letter-spacing: 3px;
  }
</style>
</head>
<body>
  <div class="flyer">
    <div class="hero-photo" role="img" aria-label="Photo of solar panels mounted on a terracotta tiled roof under a blue sky with trees"></div>

    <svg class="hero-bands" viewBox="0 0 938 900" aria-hidden="true">
      <defs>
        <linearGradient id="bandDark" x1="0" y1="0" x2="0" y2="1">
          <stop offset="0" stop-color="#2a2a2c"/>
          <stop offset="0.5" stop-color="#3c3c3f"/>
          <stop offset="1" stop-color="#2a2a2c"/>
        </linearGradient>
      </defs>
      <polygon points="0,480 320,572 938,492 938,548 320,584 0,548" fill="var(--cyan-light)"/>
      <polygon points="0,520 320,580 938,530 938,548 320,584 0,548" fill="var(--teal)" opacity="0.6"/>
      <polygon points="0,546 320,582 938,560 938,812 320,838 0,800" fill="url(#bandDark)"/>
      <polygon points="0,800 320,838 938,812 938,840 320,844 0,885" fill="var(--cyan-light)"/>
      <polygon points="0,830 320,842 0,885" fill="var(--teal)" opacity="0.7"/>
    </svg>

    <div class="headline">
      <div class="headline-kicker">Effective System</div>
      <div class="headline-main">Do it Right</div>
    </div>

    <div class="inset-photo" role="img" aria-label="Photo of applicators torching a waterproofing membrane onto a flat roof"></div>

    <p class="promise">By utilising our products and services<br>will leverage the value of the properties<br><span class="promise-accent">and protect your investment</span></p>

    <section class="provide">
      <h2 class="section-title">We provide:</h2>
      <p class="body-text">Consultation and system to solve any building problems.</p>
      <ul class="bullet-list">
        <li>E.g. tiling system</li>
        <li>Concrete repair system</li>
        <li>Waterproofing system</li>
        <li>Green roof system</li>
      </ul>
    </section>

    <section class="mission">
      <h2 class="section-title">Our mission:</h2>
      <ul class="bullet-list">
        <li>To provide consultancy</li>
        <li>Services to repair</li>
      </ul>
      <p class="body-text">to restpre and to add avlue to properties throughout the lifecycle of the building resulting in greater whole value hence not limited to developer but to end user protecting their investment with the quality products and services we provide</p>
    </section>

    <section class="philosophy">
      <h2 class="section-title">Our philosophy:</h2>
      <div class="tick-list">
        <div class="tick-col">
          <li><svg width="12" height="11" viewBox="0 0 12 11"><path d="M1 6 L4.5 9.5 L11 1" fill="none" stroke="var(--teal)" stroke-width="2.2"/></svg><span>Passion towards<br>commitment</span></li>
          <li><svg width="12" height="11" viewBox="0 0 12 11"><path d="M1 6 L4.5 9.5 L11 1" fill="none" stroke="var(--teal)" stroke-width="2.2"/></svg><span>Quality</span></li>
        </div>
        <div class="tick-col">
          <li><svg width="12" height="11" viewBox="0 0 12 11"><path d="M1 6 L4.5 9.5 L11 1" fill="none" stroke="var(--teal)" stroke-width="2.2"/></svg><span>Knowledge</span></li>
          <li><svg width="12" height="11" viewBox="0 0 12 11"><path d="M1 6 L4.5 9.5 L11 1" fill="none" stroke="var(--teal)" stroke-width="2.2"/></svg><span>Good practice<br>and result</span></li>
        </div>
      </div>
    </section>

    <div class="brand-backdrop" role="img" aria-label="Faint photo of a hand applying sealant"></div>
    <div class="brand-name">Mardolin</div>

    <footer class="footer">mardolinbuild.com</footer>
  </div>
</body>
</html>
```